Australian new start up company needs a Logo & Web Design

We need a smart, simple logo and web design for a new start up company based in Melbourne Australia called "Merchant Harbour Network". The logo is to be used on all marketing materials. The website is the primary interface of the company.

Our initial phase (launch) will provide a B2B directory service, resources and solutions.
A.) By listing on our site, small businesses can generate sales for their business. Regardless of where they might be located in the world, then can sell to Australian small businesses.
B.)Through our resource centre, small businesses can find practical and up to date resources for their business in pre-start up, start up, growth, maintenance and succession planning or exit stage.
C.)And on our site, we'll offer time and money saving solutions. These solutions can be packaged solutions (ie. Car Branding = including design, print and application onto the vehicle at a discounted price). Customers can also contact us if they want to advertise their business solution.

Eventually, there will be a total of five services inclusive of the directory described above (ie. business classifieds, link to Asian businesses, expos/seminars listing, etc). We hope to see this site grow over the next 18 months. All services will be aimed at servicing small businesses. Individuals through to large businesses located any where in the world can service these small businesses.

We would like to see designs that are professional. They should communicate growth, trust, professionalism and forward thinking.

Target Market(s)

Small Businesses (ie. employ up to 150 employees)

Industry/Entity Type

Business

Requirements
Must have
• We have attached some of the current files that we have designed ourselves. We feel that our material is lacking in appeal, professionalism and consistency. However, it does give a good idea of the requirements needed such as login, directory on the frontpage, etc. The wording is not final, as we are trying to finalise the design first. The logo was simply a placeholder as that definitely needs to be designed.

We want a logo and website that sticks in people's minds, its memorable.

We want a website that is EASY to use and navigate.
Nice to have
• Eventually, there will be a total of five services inclusive of the directory described above (ie. business classifieds, Asian businesses, expos/seminars listing, etc). They are very different types of services. The common thread is that all services will be aimed at servicing small businesses.

The winning design will need to help us to visualize how their design suits our future growth.

```html
<!DOCTYPE html>
<html lang="en">
<head>
<meta charset="utf-8">
<title>Merchant Harbour Network</title>
<link rel="stylesheet" href="https://fonts.googleapis.com/css2?family=Open+Sans:wght@400;600;700&display=swap">
<style>
  :root{
    --purple:#8b4fa3;
    --purple-dark:#6e3788;
    --purple-soft:#c6a6d2;
    --teal:#2e6b86;
    --teal-dark:#235770;
    --teal-soft:#8fb6c8;
    --green:#2f8a55;
    --green-dark:#23704a;
    --green-soft:#8ec7a0;
    --ink:#222;
    --grey-text:#555;
    --hero-top:#f4f4f4;
    --hero-bottom:#d9d9d9;
    --footer:#1c1c1c;
    --field:#bbb;
  }
  *{box-sizing:border-box;margin:0;padding:0}
  html,body{width:833px;height:1200px;overflow:hidden;background:#fff;font-family:"Open Sans",Arial,sans-serif;color:var(--ink)}
  .page{position:relative;width:833px;height:1200px}

  .post-ad{position:absolute;left:458px;top:0;width:375px;height:60px;background:var(--purple);color:#fff;font-weight:700;font-size:24px;display:flex;align-items:center;justify-content:center;border-radius:0 0 0 8px;white-space:nowrap}
  .brand{position:absolute;left:50px;top:78px;display:flex;align-items:center;gap:14px;white-space:nowrap}
  .brand-mark{width:38px;height:38px;background:var(--ink);flex-shrink:0}
  .brand-name{font-size:21px;font-weight:700;color:var(--purple)}
  .login-fields{position:absolute;left:458px;top:84px;display:flex;gap:10px}
  .login-fields span{display:block;width:158px;height:28px;border:1px solid var(--field);border-radius:4px;font-size:13px;color:#888;padding:5px 8px}
  .account-links{position:absolute;right:52px;top:118px;font-size:15px;color:var(--grey-text);white-space:nowrap}

  .hero{position:absolute;left:0;top:172px;width:833px;height:422px;background:linear-gradient(var(--hero-top),var(--hero-bottom))}
  .hero-photo{position:absolute;left:0;top:0;width:390px;height:422px;background:linear-gradient(160deg,#ececec,#cfcfcf 60%,#bdbdbd)}
  .hero-copy{position:absolute;left:405px;top:52px;width:380px}
  .hero-title{font-size:17.5px;font-weight:700;color:var(--purple);line-height:1.35;padding-bottom:18px;border-bottom:2px dashed #aaa;white-space:nowrap}
  .hero-list{list-style:none;margin-top:24px}
  .hero-list li{font-size:15.5px;color:var(--grey-text);margin-bottom:28px;padding-left:28px;position:relative;white-space:nowrap}
  .hero-list li::before{content:"";position:absolute;left:4px;top:7px;width:9px;height:9px;border-radius:50%;background:var(--purple)}
  .hero-button{display:inline-block;background:var(--ink);color:#fff;font-weight:700;font-size:15px;padding:8px 30px;border-radius:5px;white-space:nowrap}

  .search{position:absolute;left:0;top:702px;width:833px;height:40px;font-size:22px;font-weight:700;white-space:nowrap}
  .search > *{position:absolute;top:0;height:38px;display:flex;align-items:center}
  .search .need{left:50px}
  .search .field{border:1px solid var(--field);border-radius:4px}
  .search .field.what{left:128px;width:252px}
  .search .place{left:397px}
  .search .field.where{left:572px;width:194px}
  .search .go{left:705px;width:73px;justify-content:center;background:var(--ink);color:#fff;font-size:15px;border-radius:5px}

  .packages{position:absolute;left:50px;top:792px;display:flex;gap:23px}
  .package{width:230px;height:286px;border-radius:8px;overflow:hidden;color:#fff}
  .package h2{font-size:16px;font-weight:700;text-align:center;padding:24px 0;height:70px;white-space:nowrap}
  .package ul{list-style:none;padding:24px 0 0 48px}
  .package li{font-size:16px;margin-bottom:20px;white-space:nowrap}
  .start h2{background:var(--purple-dark)}
  .start{background:linear-gradient(var(--purple),var(--purple-soft))}
  .growth h2{background:var(--teal-dark)}
  .growth{background:linear-gradient(var(--teal),var(--teal-soft))}
  .vehicle h2{background:var(--green-dark)}
  .vehicle{background:linear-gradient(var(--green),var(--green-soft))}

  .footer{position:absolute;left:0;top:1111px;width:833px;height:89px;background:var(--footer);color:#fff;font-size:12px}
  .footer-col{position:absolute;top:24px;line-height:28px;white-space:nowrap}
  .social{display:flex;gap:8px;margin-top:4px}
  .social span{width:22px;height:22px;border-radius:3px}
</style>
</head>
<body>
<div class="page">
  <header>
    <div class="post-ad">Post your Free Add NOW !</div>
    <div class="brand"><span class="brand-mark"></span><span class="brand-name">Merchant Harbour Network</span></div>
    <div class="login-fields"><span>Username</span><span>Password</span></div>
    <div class="account-links">Login &nbsp;|&nbsp; Signup</div>
  </header>

  <section class="hero">
    <div class="hero-photo" role="img" aria-label="Photo of a cheerful businesswoman with a laptop, arms raised in celebration"></div>
    <div class="hero-copy">
      <h1 class="hero-title">Online directory, dedicated to servicing<br>Australian Small Businesses</h1>
      <ul class="hero-list">
        <li>Advertise for as little as $2/month</li>
        <li>Generate sales, increase brand awareness</li>
        <li>Limited time business offers</li>
        <li>Small Business resource centre</li>
      </ul>
      <span class="hero-button">See how it works</span>
    </div>
  </section>

  <section class="search">
    <span class="need">I need</span><span class="field what"></span>
    <span class="place">Location</span><span class="field where"></span>
    <span class="go">Get it</span>
  </section>

  <section class="packages">
    <div class="package start"><h2>Start up Package</h2>
      <ul><li>Logo Design</li><li>Website Design</li><li>Stationery</li><li>Directory Listing</li></ul></div>
    <div class="package growth"><h2>Biz Growth Package</h2>
      <ul><li>24 hours of</li><li>Business Coaching</li><li>go Directory Listing</li></ul></div>
    <div class="package vehicle"><h2>Vehicle Advertising</h2>
      <ul><li>Artwork Printing</li><li>Vehicle Placement</li><li>go Directory Listing</li></ul></div>
  </section>

  <footer class="footer">
    <div class="footer-col" style="left:50px">How it works<br>Post your add</div>
    <div class="footer-col" style="left:172px">Login<br>Contact us</div>
    <div class="footer-col" style="left:278px">Resource Centre<br>Asia Link</div>
    <div class="footer-col" style="left:425px">Terms &amp; Conditions<br>Privacy Policy</div>
    <div class="footer-col" style="left:645px">Follow us
      <div class="social"><span style="background:#e08a2a"></span><span style="background:#3b5b9a"></span><span style="background:#3aa6dc"></span><span style="background:#c8312b"></span></div>
    </div>
  </footer>
</div>
</body>
</html>
```